Orthopaedic Clinic Needs facebook page

Orthopaedic Clinic needs facebook page. The name of our clinic is Larchmont Orthopaedics. We focus on hip and knee orthopaedic conditions, as well as general orthopaedics. The main services are total knee replacements, total hip replacements, sports injury of the knee, hip fractures. Unique selling points of our service would be 1. Patient Centred Care, 2. Value Driven, 3. 2 Double-Fellowship Trained Surgeons.

Colour scheme should fit the logo design and be within the general colour recommendations of a medical clinic.

The design should be modern, eye catching, draws the end user to the website.

We would like to design our facebook page for future social media marketing.
In accordance with local advertisement regulations pertaining to medical clinics, no statements must have any information or laudatory statements such as the use of best, better, breakthrough, champions, or any statements that imply superiority and that may create unjustified expectations of services.

Target Market(s)

Patients
Friends family and relatives of patients.

Font styles to use
Serif
Sans Serif

Requirements
Must have
• My project must have my logo.

A nice colour scheme comfortable to the eye.
Nice to have
• Nice eye catching design that will draw the end user to the page.
Should not have
• Must not have any information that create unjustified expectaions.
Must not contain laudatory statements such as best, better, breakthrough, champions, or other statement that may create unjustified expecation of services.

```html
<!DOCTYPE html>
<html lang="en">
<head>
<meta charset="utf-8">
<title>Larchmont Orthopaedics – Facebook Cover</title>
<link rel="stylesheet" href="https://fonts.googleapis.com/css2?family=Dosis:wght@500&family=Open+Sans:wght@400;700&family=Montserrat:wght@500&display=swap">
<style>
  :root {
    --stage: #e4e4e4;
    --paper: #ffffff;
    --paper-shade: #ececec;
    --teal: #5fbab4;
    --teal-deep: #4aa9a3;
    --ink: #1f2a2e;
    --text-grey: #4a4a4a;
    --arc-dark: #2b3a3e;
    --blue-light: #1e8fd6;
    --blue-mid: #0b4fb0;
    --blue-deep: #061d6b;
  }
  * { margin: 0; padding: 0; box-sizing: border-box; }
  html, body {
    width: 1200px; height: 701px; overflow: hidden;
    background: var(--stage);
  }
  .cover {
    position: absolute; left: 0; top: 123px;
    width: 1200px; height: 455px;
    background: linear-gradient(90deg, var(--paper) 0%, var(--paper) 35%, var(--paper-shade) 70%);
    overflow: hidden;
  }
  .hero-art { position: absolute; left: 0; top: 0; width: 1200px; height: 384px; }
  .brand { position: absolute; left: 70px; top: 28px; display: flex; align-items: center; gap: 18px; }
  .brand-mark { width: 66px; height: 66px; background: var(--teal); }
  .brand-name {
    font-family: "Montserrat", sans-serif; font-weight: 500; color: var(--ink);
    line-height: 1;
  }
  .brand-name .line-1 { display: block; font-size: 34px; letter-spacing: 0.5px; }
  .brand-name .line-2 { display: block; font-size: 20px; letter-spacing: 5.5px; margin-top: 6px; }
  .section-title {
    position: absolute; left: 70px; top: 118px;
    font-family: "Dosis", sans-serif; font-weight: 500; font-size: 52px;
    color: var(--teal); line-height: 1;
  }
  .title-rule { position: absolute; left: 70px; top: 174px; width: 230px; height: 6px; }
  .title-rule .bar { position: absolute; left: 0; top: 0; width: 63px; height: 6px; background: var(--arc-dark); }
  .title-rule .line { position: absolute; left: 63px; top: 2px; width: 167px; height: 2px; background: var(--teal); }
  .services { position: absolute; left: 72px; top: 198px; list-style: none; }
  .services li {
    display: flex; align-items: center; gap: 20px;
    height: 42px;
    font-family: "Open Sans", sans-serif; font-weight: 400; font-size: 29px;
    color: var(--text-grey);
  }
  .services svg { width: 19px; height: 19px; flex: none; margin-top: 6px; }
  .values-band {
    position: absolute; left: 0; top: 384px; width: 1200px; height: 71px;
    background: var(--teal);
    display: flex; align-items: center; padding-left: 70px;
    font-family: "Open Sans", sans-serif; font-weight: 700; font-size: 26px;
    color: var(--ink); white-space: nowrap;
  }
  .values-band .sep { margin: 0 14px; }
</style>
</head>
<body>
  <main class="cover">
    <svg class="hero-art" viewBox="0 0 1200 384" aria-hidden="false">
      <defs>
        <radialGradient id="heroBlue" cx="0.7" cy="0.4" r="0.7">
          <stop offset="0" stop-color="var(--blue-mid)" />
          <stop offset="0.55" stop-color="#0a3a98" />
          <stop offset="1" stop-color="var(--blue-deep)" />
        </radialGradient>
      </defs>
      <path class="hero-arc" d="M745 0 Q555 192 705 384 L725 384 Q569 192 773 0 Z" fill="var(--arc-dark)" />
      <path class="hero-image" role="img" aria-label="Illustration of a kneeling figure with highlighted knee, hip and ankle joints in glowing blue X-ray style"
            d="M773 0 Q569 192 725 384 L1200 384 L1200 0 Z" fill="url(#heroBlue)" />
    </svg>

    <div class="brand">
      <div class="brand-mark"></div>
      <div class="brand-name">
        <span class="line-1">LARCHMONT</span>
        <span class="line-2">ORTHOPAEDICS</span>
      </div>
    </div>

    <h1 class="section-title">What we do</h1>
    <div class="title-rule"><span class="bar"></span><span class="line"></span></div>

    <ul class="services">
      <li><svg viewBox="0 0 20 20"><circle cx="10" cy="10" r="8.5" fill="none" stroke="var(--teal-deep)" stroke-width="1.6"/><path d="M6 10.2 L9 13 L14.5 7" fill="none" stroke="var(--teal-deep)" stroke-width="1.8" stroke-linecap="round"/></svg>Total knee replacements</li>
      <li><svg viewBox="0 0 20 20"><circle cx="10" cy="10" r="8.5" fill="none" stroke="var(--teal-deep)" stroke-width="1.6"/><path d="M6 10.2 L9 13 L14.5 7" fill="none" stroke="var(--teal-deep)" stroke-width="1.8" stroke-linecap="round"/></svg>Total hip replacements</li>
      <li><svg viewBox="0 0 20 20"><circle cx="10" cy="10" r="8.5" fill="none" stroke="var(--teal-deep)" stroke-width="1.6"/><path d="M6 10.2 L9 13 L14.5 7" fill="none" stroke="var(--teal-deep)" stroke-width="1.8" stroke-linecap="round"/></svg>Sports injury of the knee</li>
      <li><svg viewBox="0 0 20 20"><circle cx="10" cy="10" r="8.5" fill="none" stroke="var(--teal-deep)" stroke-width="1.6"/><path d="M6 10.2 L9 13 L14.5 7" fill="none" stroke="var(--teal-deep)" stroke-width="1.8" stroke-linecap="round"/></svg>Hip fractures</li>
    </ul>

    <div class="values-band">
      Patient Centred Care<span class="sep">|</span>Value Driven<span class="sep">|</span>2 Double-Fellowship Trained Surgeons
    </div>
  </main>
</body>
</html>
```